Voluxen

Dear designers!We need to update design our packing box. Could you offer some variants according our old design?We new manufacture of powder coatings in Estonia. We want to rebrand our box. What you can offer, how do see it? Our main idea in business is innovation . Could you do not change colors cardinally, please. Plus / minus the same colors (maybe grey or light blue)

```html
<!DOCTYPE html>
<html lang="en">
<head>
<meta charset="utf-8">
<title>Voluxen – Powder Coatings Box</title>
<link rel="stylesheet" href="https://fonts.googleapis.com/css2?family=Anton&family=Roboto:wght@400;700&display=swap">
<style>
  :root{
    --blue:#22a6dc;
    --ink:#272926;
    --pale:#7ccdee;
    --paper:#ffffff;
  }
  html,body{margin:0;padding:0;overflow:hidden;background:var(--paper);}
  .canvas{display:block;width:1200px;height:760px;}
  .display{font-family:"Anton",Impact,sans-serif;}
  .sans{font-family:"Roboto",Arial,sans-serif;}
  .brand{font-family:"Roboto",Arial,sans-serif;font-weight:700;}
  .fill-blue{fill:var(--blue);}
  .fill-ink{fill:var(--ink);}
  .fill-pale{fill:var(--pale);}
  .fill-paper{fill:var(--paper);}
  .panel-label{font-family:"Anton",Impact,sans-serif;fill:#000;}
  .stroke-ink{stroke:var(--ink);fill:none;}
  .cell-line{stroke:var(--ink);stroke-width:.5;}
</style>
</head>
<body>
<svg class="canvas" viewBox="0 0 1200 760" xmlns="http://www.w3.org/2000/svg">
  <defs>
    <symbol id="icon-this-way-up" viewBox="0 0 25 25">
      <rect width="25" height="25" class="fill-blue"/>
      <g class="stroke-ink" stroke-width="1.8">
        <path d="M9 19V7M5.5 10.5 9 6.5l3.5 4M16 19V7M12.5 10.5 16 6.5l3.5 4M5 21h15"/>
      </g>
    </symbol>
    <symbol id="icon-keep-dry" viewBox="0 0 25 25">
      <rect width="25" height="25" class="fill-blue"/>
      <g class="stroke-ink" stroke-width="1.4">
        <path d="M4 12a8.5 6 0 0 1 17 0Z"/>
        <path d="M12.5 12v7a1.8 1.8 0 0 1-3.6 0"/>
        <path d="M6 4v2M10 3v2M15 3v2M19 4v2"/>
      </g>
    </symbol>
    <symbol id="icon-temperature" viewBox="0 0 25 25">
      <rect width="25" height="25" class="fill-blue"/>
      <g class="stroke-ink" stroke-width="1.2">
        <rect x="10.5" y="3" width="4" height="15" rx="2"/>
        <path d="M15 6h3M15 9h3M15 12h3"/>
      </g>
      <circle cx="12.5" cy="19.5" r="3" class="fill-ink"/>
    </symbol>
    <symbol id="icon-keep-from-heat" viewBox="0 0 25 25">
      <rect width="25" height="25" class="fill-blue"/>
      <circle cx="12.5" cy="8" r="3" class="fill-ink"/>
      <g class="stroke-ink" stroke-width="1.2">
        <path d="M12.5 2v1.5M12.5 12.5V14M6.5 8H8M17 8h1.5M8.3 3.8l1 1M15.7 11.2l1 1M16.7 3.8l-1 1M8.3 12.2l1-1"/>
      </g>
      <rect x="7" y="15" width="11" height="7" class="fill-ink"/>
    </symbol>
  </defs>

  <!-- Front and back panel -->
  <g class="panel panel-front" transform="translate(332 42)">
    <rect width="279" height="263" class="fill-blue"/>
    <rect width="279" height="36" class="fill-ink"/>
    <g class="sans fill-paper" font-size="6.4">
      <text x="38" y="13" text-anchor="middle">PULVER LACKE</text>
      <text x="38" y="20.5" text-anchor="middle">VERNICI IN POLVERE</text>
      <text x="38" y="28" text-anchor="middle">ПОРОШКОВАЯ КРАСКА</text>
    </g>
    <text x="270" y="24" text-anchor="end" font-size="14" class="brand fill-blue">VOLUXEN</text>
    <text x="10" y="189" font-size="74" textLength="216" lengthAdjust="spacingAndGlyphs" class="display fill-ink">POWDER</text>
    <rect y="193" width="279" height="70" class="fill-ink"/>
    <text x="10" y="254" font-size="72" textLength="250" lengthAdjust="spacingAndGlyphs" class="display fill-blue">COATINGS</text>
  </g>
  <text x="472" y="349" font-size="36" text-anchor="middle" textLength="183" lengthAdjust="spacingAndGlyphs" class="panel-label">Front and back</text>

  <!-- Left side panel -->
  <g class="panel panel-left" transform="translate(687 40)">
    <rect width="179" height="263" class="fill-blue"/>
    <rect width="179" height="37" class="fill-ink"/>
    <use href="#icon-this-way-up" x="6" y="6" width="25" height="25"/>
    <use href="#icon-keep-dry" x="54" y="6" width="25" height="25"/>
    <use href="#icon-temperature" x="102" y="6" width="25" height="25"/>
    <use href="#icon-keep-from-heat" x="149" y="6" width="25" height="25"/>
    <rect class="handle-cutout stroke-ink" x="58" y="47" width="64" height="22" rx="11" stroke-width="1.2"/>
    <text x="174" y="160" text-anchor="end" font-size="14" class="brand fill-pale">VOLUXEN</text>

    <g class="safety-table" transform="translate(3 173)">
      <rect width="173" height="85" class="fill-paper"/>
      <g class="fill-ink">
        <rect x="1" y="1" width="41" height="5"/>
        <rect x="44.3" y="1" width="41" height="5"/>
        <rect x="87.6" y="1" width="41" height="5"/>
        <rect x="130.9" y="1" width="41" height="5"/>
      </g>
      <g class="fill-blue">
        <rect x="36" y="1.8" width="5" height="3.4"/>
        <rect x="79.3" y="1.8" width="5" height="3.4"/>
        <rect x="122.6" y="1.8" width="5" height="3.4"/>
        <rect x="165.9" y="1.8" width="5" height="3.4"/>
      </g>
      <g class="sans fill-paper" font-size="3.2" font-weight="700">
        <text x="18" y="4.8" text-anchor="middle">ACHTUNG</text>
        <text x="61" y="4.8" text-anchor="middle">WARNING</text>
        <text x="104" y="4.8" text-anchor="middle">ATTENZIONE</text>
        <text x="147" y="4.8" text-anchor="middle">ВНИМАНИЕ</text>
      </g>
      <g class="cell-line">
        <path d="M43.3 1v83M86.6 1v83M129.9 1v83"/>
      </g>
      <g class="sans fill-ink" font-size="3">
        <text x="2" y="12">Trocken lagern.</text>
        <text x="2" y="17">Unter 30 °C halten.</text>
        <text x="2" y="22">Staub vermeiden.</text>
        <text x="2" y="27">Gut lüften.</text>
        <text x="2" y="32">Nicht einatmen.</text>
        <text x="2" y="37">Handschuhe tragen.</text>
        <text x="2" y="42">Von Kindern fernhalten.</text>
        <text x="2" y="47">Fern von Zündquellen.</text>
        <text x="45.3" y="12">Keep dry.</text>
        <text x="45.3" y="17">Store below 30 °C.</text>
        <text x="45.3" y="22">Avoid dust.</text>
        <text x="45.3" y="27">Ventilate well.</text>
        <text x="45.3" y="32">Do not inhale.</text>
        <text x="45.3" y="37">Wear gloves.</text>
        <text x="45.3" y="42">Keep from children.</text>
        <text x="45.3" y="47">Keep from ignition.</text>
        <text x="88.6" y="12">Conservare all'asciutto.</text>
        <text x="88.6" y="17">Sotto 30 °C.</text>
        <text x="88.6" y="22">Evitare polvere.</text>
        <text x="88.6" y="27">Aerare bene.</text>
        <text x="88.6" y="32">Non inalare.</text>
        <text x="88.6" y="37">Usare guanti.</text>
        <text x="88.6" y="42">Lontano dai bambini.</text>
        <text x="88.6" y="47">Lontano da fiamme.</text>
        <text x="131.9" y="12">Хранить в сухом месте.</text>
        <text x="131.9" y="17">Ниже 30 °C.</text>
        <text x="131.9" y="22">Избегать пыли.</text>
        <text x="131.9" y="27">Проветривать.</text>
        <text x="131.9" y="32">Не вдыхать.</text>
        <text x="131.9" y="37">Работать в перчатках.</text>
        <text x="131.9" y="42">Беречь от детей.</text>
        <text x="131.9" y="47">Вдали от огня.</text>
      </g>
    </g>
  </g>
  <text x="777" y="346" font-size="36" text-anchor="middle" textLength="106" lengthAdjust="spacingAndGlyphs" class="panel-label">Left Side</text>

  <!-- Top side panel -->
  <g class="panel panel-top" transform="translate(336 424)">
    <rect width="271" height="189" class="fill-blue"/>
    <text x="6" y="90" font-size="35" textLength="107" lengthAdjust="spacingAndGlyphs" class="display fill-ink">POWDER</text>
    <rect y="93" width="271" height="96" class="fill-ink"/>
    <text x="6" y="126" font-size="35" textLength="123" lengthAdjust="spacingAndGlyphs" class="display fill-blue">COATINGS</text>
    <text x="6" y="178" font-size="14" class="brand fill-blue">VOLUXEN</text>
    <g class="sans fill-paper" font-size="6.4" text-anchor="end">
      <text x="266" y="169">PULVER LACKE</text>
      <text x="266" y="176">VERNICI IN POLVERE</text>
      <text x="266" y="183">ПОРОШКОВАЯ КРАСКА</text>
    </g>
  </g>
  <text x="472" y="673" font-size="36" text-anchor="middle" textLength="107" lengthAdjust="spacingAndGlyphs" class="panel-label">Top Side</text>

  <!-- Right side panel -->
  <g class="panel panel-right" transform="translate(688 398)">
    <rect width="177" height="264" class="fill-blue"/>
    <rect width="177" height="37" class="fill-ink"/>
    <use href="#icon-this-way-up" x="6" y="6" width="25" height="25"/>
    <use href="#icon-keep-dry" x="54" y="6" width="25" height="25"/>
    <use href="#icon-temperature" x="101" y="6" width="25" height="25"/>
    <use href="#icon-keep-from-heat" x="148" y="6" width="25" height="25"/>
    <rect class="handle-cutout stroke-ink" x="57" y="46" width="64" height="21" rx="10.5" stroke-width="1.2"/>
    <text x="171" y="185" text-anchor="end" font-size="14" class="brand fill-pale">VOLUXEN</text>

    <g class="office-table" transform="translate(7 194)">
      <rect width="163" height="65" class="fill-paper"/>
      <rect width="163" height="7" class="fill-ink"/>
      <text x="81.5" y="5" text-anchor="middle" font-size="4.2" class="sans fill-blue">Адреса торговых представительств</text>
      <g class="cell-line" fill="none">
        <rect x=".25" y=".25" width="162.5" height="64.5"/>
        <path d="M54.3 7v58M108.6 7v58M0 26.3h163M0 45.6h163"/>
      </g>
      <g class="sans fill-ink" font-size="2.8">
        <g transform="translate(2 11)">
          <text font-weight="700">Санкт-Петербург</text>
          <text y="3.5">ул. Лесная, 1</text>
          <text y="7">тел. 000-00-01</text>
          <text y="10.5">spb@voluxen.ee</text>
        </g>
        <g transform="translate(56.3 11)">
          <text font-weight="700">Новосибирск</text>
          <text y="3.5">ул. Садовая, 2</text>
          <text y="7">тел. 000-00-02</text>
          <text y="10.5">nsk@voluxen.ee</text>
        </g>
        <g transform="translate(110.6 11)">
          <text font-weight="700">Екатеринбург</text>
          <text y="3.5">ул. Речная, 3</text>
          <text y="7">тел. 000-00-03</text>
          <text y="10.5">ekb@voluxen.ee</text>
        </g>
        <g transform="translate(2 30.3)">
          <text font-weight="700">Москва</text>
          <text y="3.5">ул. Полевая, 4</text>
          <text y="7">тел. 000-00-04</text>
          <text y="10.5">msk@voluxen.ee</text>
        </g>
        <g transform="translate(56.3 30.3)">
          <text font-weight="700">Красноярск</text>
          <text y="3.5">ул. Новая, 5</text>
          <text y="7">тел. 000-00-05</text>
          <text y="10.5">krs@voluxen.ee</text>
        </g>
        <g transform="translate(110.6 30.3)">
          <text font-weight="700">Челябинск</text>
          <text y="3.5">ул. Южная, 6</text>
          <text y="7">тел. 000-00-06</text>
          <text y="10.5">chl@voluxen.ee</text>
        </g>
        <g transform="translate(2 49.6)">
          <text font-weight="700">Самара</text>
          <text y="3.5">ул. Мирная, 7</text>
          <text y="7">тел. 000-00-07</text>
          <text y="10.5">smr@voluxen.ee</text>
        </g>
        <g transform="translate(56.3 49.6)">
          <text font-weight="700">Минск</text>
          <text y="3.5">ул. Озёрная, 8</text>
          <text y="7">тел. 000-00-08</text>
          <text y="10.5">mns@voluxen.ee</text>
        </g>
      </g>
    </g>
  </g>
  <text x="777" y="709" font-size="36" text-anchor="middle" textLength="127" lengthAdjust="spacingAndGlyphs" class="panel-label">Right Side</text>
</svg>
</body>
</html>
```